New Creative Busines Card

Hi Lead Designer,

How are you going?

I was hoping you can help me design the perfect business card for my new business. I have listed below some background information about the business and the concept to help with your design. I'm open to any form of creative ideas, but would like to have two types of colour schemes one dark color and one light.

I would like to have a dark set of design and a light (One design with one in black or dark background and one with light background to compare the contrast since the business card will be double sided one) I imagine this will be pretty easy to change the background of the design. Would prefer one side to have all the details and the other will just have a amazing logo (K7) to give it the finishing touch.

Feel free to email me if you have any questions.

Business Structure and design concepts:

Name of the business: K7 Advisory
Business: Dating agency and event management (Date night etc)
Concept: The main focus will be the K7 ( As some sort of a heart shape like logo) be creative
Details to include in the card will be general details like Name, Title: , Email, mobile, website (Contact details will be given later).

The rest of the idea is up to you, feel free to go crazy with your creative ideas.

Thank you for your help in advance, may the best candidate win~!

Target Market(s)

Target market will be Professional, Elegant, young and ambitious people.

Industry/Entity Type

Business

Requirements
Must have
• Focus on the K7 (as some sort of a heart shape logo). Since this is a double sides design would prefer on one side to focus on the just the K7 logo and the other side with a smaller version of the logo (with it or without) and all the details such as Name, Title, Mobile, Email, Website. Please have the design in landscape format.Not fuss with the Font as long as it is easy to read.
Nice to have
• Different Contrast in colours (keep it simple) one side dark colour scheme and one side light. Prefer to have 3-4 colours (not overwhelm with too many colours) to keep it simple and elegant.
Should not have
• Too colours, main focus is should be the K7 logo not the colours

```html
<!DOCTYPE html>
<html lang="en">
<head>
<meta charset="utf-8">
<title>K7 Advisory – Business Card</title>
<link href="https://fonts.googleapis.com/css2?family=Sorts+Mill+Goudy&display=swap" rel="stylesheet">
<style>
  :root {
    --plum: #8c2260;
    --rose: #e3097f;
    --ink: #2b2b2b;
    --white: #ffffff;
    --mist: #e4d8e1;
    --canvas: #ffffff;
  }
  * { margin: 0; padding: 0; box-sizing: border-box; }
  html, body {
    width: 987px; height: 1200px; overflow: hidden;
    background: var(--canvas);
    font-family: "Sorts Mill Goudy", "Times New Roman", serif;
  }
  .card {
    position: absolute; left: 115px; width: 761px;
    box-shadow: 0 0 22px rgba(0,0,0,0.18);
    overflow: hidden;
  }
  /* Front side */
  .card--front { top: 88px; height: 468px; background: var(--plum); }
  .brand-mark {
    position: absolute; left: 50%; top: 62px;
    width: 150px; height: 150px; margin-left: -75px;
    border-radius: 50%; background: var(--rose);
  }
  .brand-name {
    position: absolute; left: 0; right: 0; text-align: center;
    color: var(--white); font-weight: 400; line-height: 1;
  }
  .brand-name--code { top: 298px; font-size: 46px; }
  .brand-name--word { top: 340px; font-size: 30px; letter-spacing: 1px; }
  .tagline-band {
    position: absolute; left: 0; right: 0; bottom: 0; height: 88px;
    display: flex; align-items: center; justify-content: center;
    font-size: 31px; letter-spacing: 0.3px;
  }
  .card--front .tagline-band {
    background: radial-gradient(ellipse at center, var(--white) 30%, var(--mist) 100%);
    color: var(--plum);
  }
  /* Back side */
  .card--back {
    top: 633px; height: 470px;
    background: radial-gradient(ellipse at 45% 45%, var(--white) 25%, var(--mist) 100%);
  }
  .card--back .tagline-band { height: 86px; background: var(--plum); color: var(--white); }
  .back-mark {
    position: absolute; left: 117px; top: 102px;
    width: 110px; height: 110px; border-radius: 50%; background: var(--rose);
  }
  .back-name {
    position: absolute; left: 72px; top: 290px;
    font-size: 30px; color: var(--plum);
  }
  .contact { position: absolute; left: 412px; top: 112px; color: var(--ink); }
  .contact-name { font-size: 27px; margin-bottom: 20px; }
  .contact-list { list-style: none; }
  .contact-list li {
    display: flex; align-items: center; height: 41px;
    font-size: 25px; letter-spacing: 0.5px;
  }
  .contact-list svg { width: 22px; height: 22px; margin-right: 14px; flex: none; }
</style>
</head>
<body>
  <section class="card card--front">
    <div class="brand-mark"></div>
    <div class="brand-name brand-name--code">K7</div>
    <div class="brand-name brand-name--word">ADVISORY</div>
    <div class="tagline-band">DATING AGENCY AND EVENT MANAGEMENT</div>
  </section>

  <section class="card card--back">
    <div class="back-mark"></div>
    <div class="back-name">K7 Advisory</div>
    <div class="contact">
      <p class="contact-name">Name Surname</p>
      <ul class="contact-list">
        <li>
          <svg viewBox="0 0 24 24" aria-hidden="true"><path fill="#8c2260" d="M6.6 2.5l3 3.2-1.8 2.6c1.2 2.7 3.3 4.9 6 6.2l2.6-1.8 3.2 3-1.8 3.4C10.4 19 4.8 13.3 3.2 5l3.4-2.5z"/></svg>
          123-456-7890
        </li>
        <li>
          <svg viewBox="0 0 24 24" aria-hidden="true"><rect x="6" y="2" width="12" height="20" rx="2" fill="none" stroke="#8c2260" stroke-width="2"/><circle cx="12" cy="18" r="1.3" fill="#8c2260"/></svg>
          123-456-7888
        </li>
        <li>
          <svg viewBox="0 0 24 24" aria-hidden="true"><rect x="2" y="5" width="20" height="14" fill="none" stroke="#8c2260" stroke-width="2"/><path d="M2 5l10 8 10-8" fill="none" stroke="#8c2260" stroke-width="2"/></svg>
          name@mailbox.com
        </li>
        <li>
          <svg viewBox="0 0 24 24" aria-hidden="true"><g fill="none" stroke="#8c2260" stroke-width="1.6"><circle cx="12" cy="12" r="10"/><ellipse cx="12" cy="12" rx="4.5" ry="10"/><path d="M2 12h20M4 7h16M4 17h16"/></g></svg>
          www.name.com
        </li>
      </ul>
    </div>
    <div class="tagline-band">DATING AGENCY AND EVENT MANAGEMENT</div>
  </section>
</body>
</html>
```